used car dealership needs new business card design.

Used car dealership. We have a new location and building color is bright red orange, with black trim. we want business cards to match these colors. we have uploaded our current logo to be used on business card. resolution of our logo is not very good. we are looking for it to be modern, and appeal to men and women ages 18-55. We are based in San Antonio TX so the Verdell is cutout design of our logo is the reasoning behind the logo.
Target Market(s)
Hispanic and Caucasian male & females ages 18-55
Industry/Entity Type
Car Dealer
Logo Text
Name: Copper Ridge Auto & Trucks, Address: 5127 Marlowe Crest Rd, San Antonio, TX 78364, Phone Number: 210-555-0187, Fax: 210-555-0243, Email: sales.copperridgeauto@mailpost-demo.net, Website: www.friendwall-demo.net/copperridgeautoKV

```html
<!DOCTYPE html>
<html lang="en">
<head>
<meta charset="utf-8">
<title>Copper Ridge Auto &amp; Trucks — Business Card</title>
<link rel="stylesheet" href="https://fonts.googleapis.com/css2?family=Oxygen:wght@400&display=swap">
<style>
  :root {
    --backdrop: #1b1b1b;
    --card: #080808;
    --card-edge: #2a2a2a;
    --ink: #d4d4d4;
    --brand-ink: #8a8a8a;
    --brand-accent: #e8512a;
  }
  html, body {
    margin: 0;
    padding: 0;
    width: 1200px;
    height: 1000px;
    overflow: hidden;
    background: var(--backdrop);
  }
  .canvas {
    width: 1200px;
    height: 1000px;
    display: flex;
    align-items: center;
    justify-content: center;
  }
  .business-card {
    position: relative;
    width: 840px;
    height: 480px;
    background: var(--card);
    border: 1px solid var(--card-edge);
    border-radius: 4px;
    box-sizing: border-box;
    overflow: hidden;
  }
  .brand-mark {
    position: absolute;
    right: 56px;
    top: 72px;
    display: flex;
    align-items: center;
    gap: 18px;
    font-family: "Oxygen", sans-serif;
    font-weight: 400;
    color: var(--brand-ink);
  }
  .brand-dot {
    width: 22px;
    height: 22px;
    border-radius: 50%;
    background: var(--brand-accent);
    flex: none;
  }
  .brand-name {
    margin: 0;
    font-size: 34px;
    line-height: 1.2;
    font-weight: 400;
    letter-spacing: 0.5px;
  }
  .contact-block {
    position: absolute;
    left: 56px;
    bottom: 52px;
    margin: 0;
    font-family: "Oxygen", sans-serif;
    font-style: normal;
    font-size: 27px;
    line-height: 1.22;
    color: var(--ink);
    letter-spacing: 0.2px;
  }
  .contact-line {
    display: block;
  }
</style>
</head>
<body>
  <main class="canvas">
    <section class="business-card" aria-label="Copper Ridge Auto &amp; Trucks business card">
      <div class="brand-mark">
        <span class="brand-dot" aria-hidden="true"></span>
        <h1 class="brand-name">Copper Ridge<br>Auto &amp; Trucks</h1>
      </div>
      <address class="contact-block">
        <span class="contact-line">5127 Marlowe Crest Rd</span>
        <span class="contact-line">San Antonio, TX 78364</span>
        <span class="contact-line">Phone:210-555-0187</span>
        <span class="contact-line">Fax: 210-555-0243</span>
        <span class="contact-line">sales.copperridgeauto@mailpost-demo.net</span>
        <span class="contact-line">www.friendwall-demo.net/copperridgeautoKV</span>
      </address>
    </section>
  </main>
</body>
</html>
```